QX27

We want a trendy packaging design for our mobile accessories. Initially we will be offering TPU cases to our retail customers and than we will introduce other similar accessories such as car chargers, AC chargers, data cables etc..
We would like to see designs that are unique, practical and appealing to the general audience.
Updates

Hi Everyone

There is guaranteed payment for the best designer of this packaging.

thanks

Reason: Hi All This will give you all more time to submit your designs :) regards

Target Market(s)

Telco retail store customers

Industry/Entity Type

Retail

Requirements
Must have
• Colorful , Fun , Sexy

```html
<!DOCTYPE html>
<html lang="en">
<head>
<meta charset="utf-8">
<title>QX27 Mobile Accessories Packaging</title>
<link rel="stylesheet" href="https://fonts.googleapis.com/css2?family=PT+Sans:wght@400;700&display=swap">
<style>
  :root {
    --ink: #5b6669;
    --teal: #4fb8b2;
    --purple: #9062b4;
    --sea: #16a3a0;
    --pink: #d74c77;
    --card-top: #d3d6d7;
    --card-top-light: #eef0f0;
    --card-body: #e9eaea;
    --pattern: #d2d4d5;
    --stage: #cfd2d4;
    --label: #1d1d1d;
  }
  * { margin: 0; padding: 0; box-sizing: border-box; }
  html, body { width: 1200px; height: 954px; overflow: hidden; }
  body {
    font-family: "PT Sans", sans-serif;
    background: #ffffff;
    position: relative;
  }
  .brand-header {
    position: absolute;
    left: 83px; top: 88px;
    display: flex; align-items: center; gap: 26px;
  }
  .brand-header .mark {
    width: 62px; height: 62px; border-radius: 50%;
    background: var(--teal);
  }
  .brand-header .name {
    font-weight: 700; font-size: 70px; line-height: 1;
    color: var(--ink); letter-spacing: 2px;
  }
  .stage {
    position: absolute; left: 0; top: 240px;
    width: 1200px; height: 714px;
    background: var(--stage);
  }
  .pack {
    position: absolute; top: 304px;
    width: 290px; height: 586px;
    background: var(--card-body);
    box-shadow: 0 6px 18px rgba(0,0,0,0.25);
    overflow: hidden;
  }
  .pack svg.art { position: absolute; left: 0; top: 0; }
  .pack .logo {
    position: absolute; left: 16px; top: 128px;
    display: flex; align-items: center; gap: 12px;
  }
  .pack .logo .mark {
    width: 34px; height: 34px; border-radius: 50%;
    background: var(--teal);
  }
  .pack .logo .name {
    font-weight: 700; font-size: 36px; line-height: 1;
    color: var(--ink); letter-spacing: 1px;
  }
  .pack .label {
    position: absolute; left: 0; right: 0; top: 486px;
    text-align: center; font-size: 22px; color: var(--label);
  }
  .pack-charger { left: 86px; }
  .pack-cover { left: 454px; }
  .pack-cable { left: 822px; }
</style>
</head>
<body>
  <header class="brand-header">
    <span class="mark"></span>
    <span class="name">QX27</span>
  </header>

  <div class="stage"></div>

  <!-- Car charger pack -->
  <section class="pack pack-charger">
    <svg class="art" width="290" height="586" viewBox="0 0 290 586">
      <defs>
        <linearGradient id="top-charger" x1="0" y1="0" x2="0" y2="1">
          <stop offset="0" stop-color="var(--card-top)"/>
          <stop offset="1" stop-color="var(--card-top-light)"/>
        </linearGradient>
        <linearGradient id="photo-charger" x1="0" y1="0" x2="0" y2="1">
          <stop offset="0" stop-color="#3a3d3f"/>
          <stop offset="1" stop-color="#c4c6c7"/>
        </linearGradient>
      </defs>
      <rect x="0" y="0" width="290" height="112" fill="url(#top-charger)"/>
      <rect x="0" y="112" width="290" height="130" fill="var(--card-top-light)"/>
      <rect x="0" y="242" width="290" height="344" fill="var(--pattern)" role="img" aria-label="Swirling grey and white stripe pattern"/>
      <path d="M82,44 H128 Q135,30 145,30 Q155,30 162,44 H208 Q218,44 218,55 Q218,66 208,66 H82 Q72,66 72,55 Q72,44 82,44 Z" fill="#8d9496"/>
      <path d="M0,238 H290 V262 H264 Q245,262 245,290 V372 A100,96 0 0 1 45,372 V290 Q45,262 26,262 H0 Z" fill="var(--purple)"/>
      <path d="M62,188 Q62,176 76,176 H214 Q228,176 228,188 V366 A83,72 0 0 1 62,366 Z" fill="url(#photo-charger)" role="img" aria-label="Photo of a black car charger with coiled cable"/>
      <line x1="0" y1="548" x2="58" y2="548" stroke="var(--purple)" stroke-width="3"/>
      <rect x="58" y="538" width="12" height="20" fill="var(--purple)"/>
      <path d="M70,534 H112 Q126,534 130,544 H146 V552 H130 Q126,562 112,562 H70 Z" fill="var(--purple)"/>
    </svg>
    <div class="logo"><span class="mark"></span><span class="name">QX27</span></div>
    <p class="label">CAR CHARGER</p>
  </section>

  <!-- TPU cover pack -->
  <section class="pack pack-cover">
    <svg class="art" width="290" height="586" viewBox="0 0 290 586">
      <defs>
        <linearGradient id="top-cover" x1="0" y1="0" x2="0" y2="1">
          <stop offset="0" stop-color="var(--card-top)"/>
          <stop offset="1" stop-color="var(--card-top-light)"/>
        </linearGradient>
        <linearGradient id="photo-cover" x1="0" y1="0" x2="0" y2="1">
          <stop offset="0" stop-color="#1e9be0"/>
          <stop offset="1" stop-color="#2a4fae"/>
        </linearGradient>
      </defs>
      <rect x="0" y="0" width="290" height="112" fill="url(#top-cover)"/>
      <rect x="0" y="112" width="290" height="130" fill="var(--card-top-light)"/>
      <rect x="0" y="242" width="290" height="344" fill="var(--pattern)" role="img" aria-label="Swirling grey and white stripe pattern"/>
      <path d="M82,44 H128 Q135,30 145,30 Q155,30 162,44 H208 Q218,44 218,55 Q218,66 208,66 H82 Q72,66 72,55 Q72,44 82,44 Z" fill="#8d9496"/>
      <path d="M0,238 H290 V262 H264 Q245,262 245,290 V372 A100,96 0 0 1 45,372 V290 Q45,262 26,262 H0 Z" fill="var(--sea)"/>
      <path d="M62,188 Q62,176 76,176 H214 Q228,176 228,188 V366 A83,72 0 0 1 62,366 Z" fill="var(--card-top-light)"/>
      <path d="M50,196 Q50,180 66,180 H226 Q242,180 242,196 V360 Q242,408 200,408 H92 Q50,408 50,360 Z" fill="url(#photo-cover)" role="img" aria-label="Photo of a blue translucent TPU phone cover"/>
      <rect x="20" y="526" width="66" height="40" rx="4" fill="none" stroke="var(--sea)" stroke-width="3"/>
      <rect x="28" y="534" width="50" height="24" rx="2" fill="var(--sea)"/>
      <circle cx="70" cy="546" r="4" fill="#ffffff"/>
    </svg>
    <div class="logo"><span class="mark"></span><span class="name">QX27</span></div>
    <p class="label">TPU COVER</p>
  </section>

  <!-- Data cable pack -->
  <section class="pack pack-cable">
    <svg class="art" width="290" height="586" viewBox="0 0 290 586">
      <defs>
        <linearGradient id="top-cable" x1="0" y1="0" x2="0" y2="1">
          <stop offset="0" stop-color="var(--card-top)"/>
          <stop offset="1" stop-color="var(--card-top-light)"/>
        </linearGradient>
        <linearGradient id="photo-cable" x1="0" y1="0" x2="0" y2="1">
          <stop offset="0" stop-color="#4a4d4f"/>
          <stop offset="1" stop-color="#bfc2c3"/>
        </linearGradient>
      </defs>
      <rect x="0" y="0" width="290" height="112" fill="url(#top-cable)"/>
      <rect x="0" y="112" width="290" height="130" fill="var(--card-top-light)"/>
      <rect x="0" y="242" width="290" height="344" fill="var(--pattern)" role="img" aria-label="Swirling grey and white stripe pattern"/>
      <path d="M82,44 H128 Q135,30 145,30 Q155,30 162,44 H208 Q218,44 218,55 Q218,66 208,66 H82 Q72,66 72,55 Q72,44 82,44 Z" fill="#8d9496"/>
      <path d="M0,238 H290 V262 H264 Q245,262 245,290 V372 A100,96 0 0 1 45,372 V290 Q45,262 26,262 H0 Z" fill="var(--pink)"/>
      <path d="M62,188 Q62,176 76,176 H214 Q228,176 228,188 V366 A83,72 0 0 1 62,366 Z" fill="url(#photo-cable)" role="img" aria-label="Photo of a black USB data cable, coiled"/>
      <line x1="0" y1="548" x2="52" y2="548" stroke="var(--pink)" stroke-width="3"/>
      <rect x="52" y="540" width="10" height="16" fill="var(--pink)"/>
      <path d="M62,536 H98 V560 H62 Z" fill="var(--pink)"/>
      <rect x="108" y="534" width="26" height="28" fill="var(--pink)"/>
      <rect x="114" y="540" width="6" height="6" fill="#ffffff"/>
      <rect x="122" y="540" width="6" height="6" fill="#ffffff"/>
      <rect x="114" y="550" width="6" height="6" fill="#ffffff"/>
      <rect x="122" y="550" width="6" height="6" fill="#ffffff"/>
    </svg>
    <div class="logo"><span class="mark"></span><span class="name">QX27</span></div>
    <p class="label">DATA CABLE</p>
  </section>
</body>
</html>
```